Veterinarian specialized in Equine (horse) sports medicine needs logo and stationary design!

New veterinary clinic only focused on horses needs logo and stationary designs. The clinic works with sport horses including jumping horses, dressage horses and polo horses (all disciplines you can find online. No racing horses). Name of clinic is StrideCare and is based in Mexico City where there is a large and elite clientele of sports horses. My main focus is orthopedics and rehabilitation.
I think logo should include horse(s), especially if they are performing a sport (like jumping, etc).

Target Market(s)

Elite horse-owners of sport horses.

Industry/Entity Type

Horseback Riding

Requirements
Must have
• Great Logo! I like bold and bright colors (no pastels), but with a professional tone.

```html
<!DOCTYPE html>
<html lang="en">
<head>
<meta charset="utf-8">
<title>StrideCare Stationery</title>
<link href="https://fonts.googleapis.com/css2?family=Cinzel:wght@500&family=Lato:wght@400;700&display=swap" rel="stylesheet">
<style>
  :root{
    --bg:#d0d1d3;
    --blue:#1a75a3;
    --blue-deep:#16699a;
    --blue-soft:#2a82ad;
    --orange:#f39b68;
    --orange-pale:#fbe3d4;
    --paper:#ffffff;
    --paper-grey:#f3f3f4;
    --ink:#333a40;
  }
  *{box-sizing:border-box;margin:0;padding:0}
  html,body{width:1200px;height:1200px;overflow:hidden;background:var(--bg)}
  body{position:relative;font-family:"Lato",sans-serif;color:var(--ink)}
  .item{position:absolute;box-shadow:4px 6px 10px rgba(0,0,0,.12)}
  .wordmark{font-family:"Cinzel",serif;font-weight:500;color:var(--blue);white-space:nowrap;line-height:1}
  .wordmark.light{color:#fff}
  .art{position:absolute}

  .brand-hero{position:absolute;left:0;top:150px;width:1200px;text-align:center}
  .brand-hero .wordmark{font-size:78px;letter-spacing:2px}
  .brand-hero .dot{display:inline-block;width:12px;height:12px;border-radius:50%;background:var(--orange);margin-left:14px;vertical-align:middle}

  /* folder */
  .folder-flap{position:absolute;left:66px;top:344px;width:44px;height:296px;background:var(--paper);clip-path:polygon(100% 0,100% 100%,0 92%,0 8%)}
  .folder-cover{left:110px;top:342px;width:217px;height:300px;background:var(--blue)}
  .folder-cover .art{left:20px;top:18px;width:180px;height:230px;background:var(--blue-soft);border-radius:40% 40% 10% 30%}
  .contact-row{position:absolute;left:50px;bottom:16px;display:flex;gap:16px;font-size:3.5px;color:#fff}
  .folder-inside{left:327px;top:342px;width:219px;height:300px;background:var(--paper)}
  .folder-inside .art{inset:0;background:linear-gradient(180deg,#f7f7f8,#eeeff1)}
  .folder-inside .wordmark{position:absolute;left:0;right:0;top:142px;text-align:center;font-size:18px}
  .folder-pocket{position:absolute;left:110px;top:642px;width:217px;height:50px;background:var(--paper);clip-path:polygon(0 0,100% 0,80% 100%,0 100%)}

  /* letterhead */
  .letterhead{left:562px;top:342px;width:212px;height:300px;background:var(--paper);padding:24px 16px 0 16px}
  .lh-head{display:flex;align-items:center;gap:8px}
  .lh-head .wordmark{font-size:10px}
  .lh-rule{flex:1;border-top:1px solid var(--blue);position:relative}
  .lh-rule span{position:absolute;right:0;top:-6px;font-size:3.5px}
  .lh-meta{display:flex;justify-content:space-between;margin-top:28px;font-size:3.5px;font-weight:700}
  .lh-body{margin-top:14px;font-size:3.4px;line-height:1.35}
  .lh-body p{margin-bottom:5px}
  .lh-sign{margin-top:8px;font-size:3.5px}
  .lh-sign b{display:block}
  .lh-sign i{display:block;width:34px;border-top:1px solid #555;margin-top:10px}
  .lh-art{position:absolute;left:70px;top:70px;width:80px;height:140px;background:var(--orange-pale);opacity:.55;border-radius:30%}
  .lh-foot{position:absolute;left:16px;right:16px;bottom:14px;border-top:1px solid var(--blue);font-size:3px;padding-top:2px}

  /* business cards */
  .card-front{left:766px;top:404px;width:136px;height:78px;background:var(--blue);display:flex;align-items:center;justify-content:center}
  .card-front .wordmark{font-size:12px}
  .card-back{left:766px;top:502px;width:136px;height:76px;background:var(--paper)}
  .card-back .art{left:0;top:2px;width:60px;height:72px;background:var(--orange-pale)}
  .card-back .info{position:absolute;right:10px;top:14px;text-align:right;font-size:3.4px;line-height:1.5}
  .card-back .wordmark{font-size:7px;margin-bottom:3px}
  .card-back .name{font-family:"Cinzel",serif;color:var(--blue);font-size:4px}

  /* spiral pad */
  .pad{left:924px;top:382px;width:169px;height:232px;background:var(--blue)}
  .pad::before{content:"";position:absolute;left:10px;right:10px;top:-6px;height:12px;background:repeating-linear-gradient(90deg,#fff 0 2px,transparent 2px 6px)}
  .pad .art{left:10px;top:30px;width:140px;height:160px;background:var(--blue-soft);border-radius:40% 40% 10% 30%}
  .pad .foot{position:absolute;right:14px;bottom:14px;text-align:center;font-size:3.5px;color:#fff}
  .pad .wordmark{font-size:10px;margin-bottom:2px}

  /* bottom letter */
  .sheet{left:126px;top:763px;width:240px;height:339px;background:var(--paper);padding:28px 26px}
  .sheet .wordmark{font-size:13px}
  .sheet .addr{font-size:4px;margin-top:5px}

  /* large envelope */
  .big-env{left:327px;top:786px;width:240px;height:340px;background:var(--paper)}
  .big-env .flap{position:absolute;left:0;right:0;top:0;height:40px;background:var(--blue);border-radius:0 0 6px 6px}
  .big-env .addr{position:absolute;left:24px;bottom:24px;font-size:4px;line-height:1.4}

  /* notebook */
  .notebook{left:595px;top:714px;width:235px;height:334px;background:var(--blue)}
  .notebook .rings{position:absolute;left:-14px;top:12px;width:24px;height:310px;background:radial-gradient(circle at 12px 6px,#fff 0 5px,transparent 5.5px) 0 0/24px 22.3px repeat-y}
  .notebook .art{left:30px;top:48px;width:160px;height:200px;background:var(--blue-soft);border-radius:40% 40% 10% 30%}
  .notebook .foot{position:absolute;right:22px;bottom:20px;text-align:center;font-size:4px;line-height:1.45;color:#fff}
  .notebook .wordmark{font-size:13px;margin-bottom:6px}

  /* DL envelope */
  .dl-front{left:864px;top:698px;width:295px;height:148px;background:var(--paper-grey)}
  .dl-front .window{position:absolute;left:21px;top:52px;width:101px;height:48px;border-radius:8px;background:linear-gradient(120deg,var(--blue-deep),#3a91bc 55%,var(--blue))}
  .dl-front .wordmark{position:absolute;right:16px;top:34px;font-size:14px}
  .dl-front .addr{position:absolute;right:16px;top:106px;text-align:right;font-size:5px;line-height:1.4}
  .dl-back{left:864px;top:865px;width:295px;height:149px;background:var(--paper-grey)}
  .dl-back .flap{position:absolute;left:0;right:0;top:0;height:49px;background:var(--blue);border-radius:0 0 10px 10px}
</style>
</head>
<body>

<header class="brand-hero">
  <span class="wordmark">StrideCare</span><span class="dot"></span>
</header>

<!-- presentation folder -->
<div class="folder-flap"></div>
<section class="item folder-cover">
  <div class="art" role="img" aria-label="Faint rearing horse illustration"></div>
  <div class="contact-row"><span>555-014-822</span><span>hola@stridecare.mx</span><span>www.stridecare.mx</span></div>
</section>
<section class="item folder-inside">
  <div class="art" role="img" aria-label="Light wavy line pattern"></div>
  <span class="wordmark">StrideCare</span>
</section>
<div class="folder-pocket"></div>

<!-- letterhead -->
<section class="item letterhead">
  <div class="lh-art" role="img" aria-label="Faint orange horse watermark"></div>
  <div class="lh-head">
    <span class="wordmark">StrideCare</span>
    <div class="lh-rule"><span>45 Calle Río, CDMX 11000</span></div>
  </div>
  <div class="lh-meta"><span>Dear, Mr.________</span><span>DATE:1/5/2018</span></div>
  <div class="lh-body">
    <p>Thank you for trusting our team with the care of your horse. This letter confirms the rehabilitation plan, follow-up visits and exercise schedule agreed during the last examination at our clinic.</p>
    <p>Thank you for trusting our team with the care of your horse. This letter confirms the rehabilitation plan, follow-up visits and exercise schedule agreed during the last examination at our clinic.</p>
    <p>Thank you for trusting our team with the care of your horse. This letter confirms the rehabilitation plan, follow-up visits and exercise schedule agreed during the last examination at our clinic.</p>
    <p>Thank you for trusting our team with the care of your horse. This letter confirms the rehabilitation plan, follow-up visits and exercise schedule agreed during the last examination at our clinic.</p>
  </div>
  <div class="lh-sign"><b>YOUR NAME</b>Designation<i></i></div>
  <div class="lh-foot">hola@stridecare.mx &nbsp; www.stridecare.mx</div>
</section>

<!-- business cards -->
<section class="item card-front"><span class="wordmark light">StrideCare</span></section>
<section class="item card-back">
  <div class="art" role="img" aria-label="Pale orange rearing horse illustration"></div>
  <div class="info">
    <div class="wordmark">StrideCare</div>
    <div class="name">ANA RIVERA</div>
    <div>Doctor</div>
    <div>555-014-822</div>
    <div>hola@stridecare.mx</div>
    <div>www.stridecare.mx</div>
    <div>45 Calle Río, CDMX 11000</div>
  </div>
</section>

<!-- spiral pad -->
<section class="item pad">
  <div class="art" role="img" aria-label="Faint rearing horse illustration"></div>
  <div class="foot"><div class="wordmark light">StrideCare</div>www.stridecare.mx</div>
</section>

<!-- letter sheet -->
<section class="item sheet">
  <div class="wordmark">StrideCare</div>
  <div class="addr">45 Calle Río, CDMX 11000</div>
</section>

<!-- large envelope -->
<section class="item big-env">
  <div class="flap"></div>
  <div class="addr">555-014-822<br>45 Calle Río, CDMX 11000<br>www.stridecare.mx</div>
</section>

<!-- notebook -->
<section class="item notebook">
  <div class="art" role="img" aria-label="Faint rearing horse illustration"></div>
  <div class="rings"></div>
  <div class="foot">
    <div class="wordmark light">StrideCare</div>
    555-014-822<br>hola@stridecare.mx<br>45 Calle Río, CDMX 11000<br>www.stridecare.mx
  </div>
</section>

<!-- DL envelope -->
<section class="item dl-front">
  <div class="window"></div>
  <span class="wordmark">StrideCare</span>
  <div class="addr">555-014-822<br>45 Calle Río, CDMX 11000<br>www.stridecare.mx</div>
</section>
<section class="item dl-back"><div class="flap"></div></section>

</body>
</html>
```